Modern and sophisticated web design for architect/designer

Vantor Loom is a Building Design & Drafting studio based in Nedlands Western Australia, providing a high quality and complete client service from concept design through Council planning approvals and building licenses to construction drawings for kitchens and bathrooms, extensions, additions, renovations and new homes.

Vantor Loom is looking for a new qwerty design that *is different from a normal* 2/3 column website. The website design must be very arty, clean and catchy. This design needs to be very different and must not look like a downloadable template.

The design must be able to display a lot of photos for the different projects.

The design must comply with W3C standards (i.e. use of fonts) and must be delivered to us in A PSD layered format.

Here are a couple of example website designs that exemplify what I am after:
1) http://www.plvm.com.au/
2) http://www.thomasvellearchitect.com/en/
3) http://quormel.com/

I particularly like numbers 1 and 2. The third, Quormel, jumps around a little between pages as it is actually several companies. I prefer the page design to remain steady if possible.

I like the very clever nature of number 1 (PLVM). It captures the interest, although slightly gimmicky, however I think it doesn't overpower. Its modern, and visual.

I like the clean elegant design of number 2 (Velle), it simply delivers everything necessary in a clear intelligent manner, its attractive, menu is clever simple to use and attractive.

I would be very happy to have either of these websites.

here is another one:
4) http://www.wnarchitect.com.au/

Although this is similarly elegant, it appears quite dated. I don't like the thumbnails that you click on in the gallery, its quite clumsy. It looks minimalist, and IS minimalist, doesn't look like there is much option to expand other than changing the pictures.

If you look at my own website:
http://www.vantorloom.com.au

I designed and built it myself without any skills or experience. I had to use a generic photo album generator which was worse than useless, the point I am trying to make is I tried to make the menu system a little unusual, I tried to keep the pages neat and tidy, and totally used the "black website" method. However I am more inclined to go with the lighter/white pages of (1) and (2) above because they tend to show photos better.
Updates

Dear Designers. 

ArtBazaarHub Administration has worked to provide a more comprehensive brief. Please review the amended description. 

Kind Regards, Gordon. 

Target Market(s)

Target market is people who are looking to renovate their home

Industry/Entity Type

Construction

Requirements
Must have
• The brief is to design a visual modern, elegant, sophisticated website for a small scale designer/photographer/architect that looks itself like it is designed. Not off the shelf, simple and dated. Basically the design itself has to exemplify me, it has to say "this guy is a designer, and he is good at it".

```html
<!DOCTYPE html>
<html lang="en">
<head>
<meta charset="utf-8">
<title>Vantor Loom — Building Design &amp; Drafting Studio</title>
<link rel="stylesheet" href="https://fonts.googleapis.com/css2?family=Roboto+Condensed:wght@400;700&family=Source+Sans+3:wght@300;400;600&display=swap">
<style>
:root{
  --ink:#2a1a18;
  --brown:#4b2a27;
  --brown-deep:#3a1f1c;
  --muted:#777;
  --line:#d9d9d9;
  --paper:#fff;
  --footer:#f1f1f1;
}
*{box-sizing:border-box;margin:0;padding:0}
html,body{width:1004px;height:1200px;overflow:hidden;background:var(--paper)}
body{position:relative;font-family:"Source Sans 3",sans-serif;color:var(--ink)}
a{color:inherit;text-decoration:none}

.site-header{position:absolute;left:0;top:0;width:1004px;height:118px}
.brand{position:absolute;left:68px;top:36px;display:flex;align-items:center;gap:10px;font-family:"Roboto Condensed",sans-serif;font-size:30px;font-weight:400;letter-spacing:3px;color:var(--ink);text-transform:uppercase}
.brand-mark{width:14px;height:14px;background:var(--brown)}
.social{position:absolute;left:624px;top:26px;display:flex;gap:8px}
.social span{width:20px;height:20px;border-radius:50%;background:#9a9a9a}
.search{position:absolute;left:712px;top:24px;width:232px;height:30px;border:1px solid var(--line);font-style:italic;font-size:12px;color:#999;padding:7px 12px}
.search svg{position:absolute;right:10px;top:7px}
.main-nav{position:absolute;right:60px;top:76px;display:flex;font-family:"Roboto Condensed",sans-serif;font-size:18px}
.main-nav a{padding:0 17px;border-left:1px solid #bbb;line-height:18px}
.main-nav a:first-child{border-left:0}
.main-nav a:last-child{padding-right:0}

.hero{position:absolute;left:0;top:118px;width:1004px;height:418px;background:var(--brown)}
.hero-photo{position:absolute;left:0;top:0;width:662px;height:418px;background:linear-gradient(120deg,#142237 0%,#2e3038 30%,#7a4b24 55%,#c07a38 70%,#3c4a1d 100%);border-right:2px solid #8d7a74}
.hero-copy{position:absolute;left:703px;top:72px;width:260px;color:#fff}
.hero-copy h1{font-weight:300;line-height:1}
.hero-copy .kicker{display:block;font-size:27px;margin-bottom:10px}
.hero-copy .title{display:block;font-size:37px}
.hero-copy p{margin-top:14px;font-size:13px;line-height:20.5px;font-weight:300;color:#eee}
.dots{display:flex;gap:3px;margin-top:14px}
.dots i{width:11px;height:11px;border-radius:50%;background:#7d6461}
.dots i:first-child{background:#fff}

.features{position:absolute;left:62px;top:503px;width:889px;height:280px;background:var(--paper);border-radius:6px;box-shadow:0 8px 14px -6px rgba(0,0,0,.18),0 0 2px rgba(0,0,0,.08)}
.feature{position:absolute;top:23px;width:268px}
.feature .thumb{height:123px;border:5px solid #fff;box-shadow:0 0 3px rgba(0,0,0,.3)}
.feature h2{margin-top:14px;font-family:"Roboto Condensed",sans-serif;font-size:21px;font-weight:700;letter-spacing:.3px;color:var(--ink)}
.feature p{margin-top:6px;font-size:13px;line-height:19px;color:var(--muted);font-weight:300}

.columns{position:absolute;left:0;top:826px;width:1004px}
.col{position:absolute;top:0}
.col-welcome{left:63px;width:290px}
.col-services{left:371px;width:287px;border-left:1px solid var(--line);padding-left:28px;height:236px;top:12px}
.col-gallery{left:657px;width:300px;border-left:1px solid var(--line);padding-left:24px;height:236px;top:12px}
.col h3{font-weight:300;font-size:24px;color:var(--ink);line-height:1.1}
.col-welcome h3 .lead{display:block;font-size:24px}
.col-welcome h3 .strong{display:block;font-weight:600;font-size:29px;margin-top:2px}
.col-welcome p{margin-top:12px;font-size:13.5px;line-height:20.5px;color:#3b2a28;font-weight:300}
.col-welcome p + p{margin-top:5px}
.col-services p{margin-top:6px;font-size:13.5px;line-height:20.5px;font-weight:300;color:#3b2a28}
.ticks{list-style:none;margin-top:12px;width:216px}
.ticks li{display:flex;align-items:center;gap:6px;font-size:13px;height:28px;border-bottom:1px solid #e6e6e6;color:var(--brown-deep)}
.gallery{display:grid;grid-template-columns:repeat(3,83px);gap:7px 7px;margin-top:12px}
.gallery div{height:79px}

.site-footer{position:absolute;left:0;top:1105px;width:1004px;height:95px;background:linear-gradient(#ececec,#fafafa)}
.site-footer small{position:absolute;left:65px;top:38px;font-size:12px;color:#666;font-weight:300}
.footer-nav{position:absolute;right:60px;top:35px;display:flex;font-family:"Roboto Condensed",sans-serif;font-size:16px}
.footer-nav a{padding:0 8px;border-left:1px solid #555;line-height:16px}
.footer-nav a:first-child{border-left:0}
.footer-nav a:last-child{padding-right:0}
</style>
</head>
<body>

<header class="site-header">
  <a class="brand" href="#"><span class="brand-mark"></span>Vantor Loom</a>
  <div class="social" aria-label="Social links"><span></span><span></span><span></span></div>
  <div class="search">Search here..
    <svg width="16" height="16" viewBox="0 0 16 16"><circle cx="6.5" cy="6.5" r="5" fill="none" stroke="#888" stroke-width="2"/><line x1="10" y1="10" x2="14.5" y2="14.5" stroke="#888" stroke-width="2.4"/></svg>
  </div>
  <nav class="main-nav">
    <a href="#">MAIN</a><a href="#">ABOUT US</a><a href="#">SERVICES</a><a href="#">PROJECTS</a><a href="#">CONTACT</a>
  </nav>
</header>

<section class="hero">
  <div class="hero-photo" role="img" aria-label="Evening view of a house entrance with a lit stacked-stone wall and garden"></div>
  <div class="hero-copy">
    <h1><span class="kicker">Building Design &amp;</span><span class="title">Drafting Studio</span></h1>
    <p>Aliquam vehicula mi at mauris. Maecenas placerat, nisl at consequat rhoncus, sem nunc gravida justo, quis eleifend arcu velit quis lacus. Morbi magna magna, tincidunt a, mattis non, imperdiet vitae</p>
    <div class="dots"><i></i><i></i><i></i><i></i></div>
  </div>
</section>

<section class="features">
  <article class="feature" style="left:25px">
    <div class="thumb" role="img" aria-label="Modern two-storey home with orange framed windows" style="background:linear-gradient(160deg,#4f7fd0 0%,#9fb7dc 40%,#8a7a6c 65%,#4a5a36 100%)"></div>
    <h2>Building License</h2>
    <p>Duis tincidunt lectus quis dui viverra vestibulum. Suspendisse vulputate aliquam dui.</p>
  </article>
  <article class="feature" style="left:310px">
    <div class="thumb" role="img" aria-label="Contemporary house facade with balcony" style="background:linear-gradient(160deg,#3c6cc6 0%,#9a8c7e 35%,#7a736c 65%,#5d6048 100%)"></div>
    <h2>Construction Services</h2>
    <p>Duis tincidunt lectus quis dui viverra vestibulum. Suspendisse vulputate aliquam dui.</p>
  </article>
  <article class="feature" style="left:601px">
    <div class="thumb" role="img" aria-label="Modern kitchen with red tiled splashback" style="background:linear-gradient(160deg,#5a4a44 0%,#8a3a2a 40%,#6c5a4e 65%,#c9b9a6 100%)"></div>
    <h2>Other Services</h2>
    <p>Duis tincidunt lectus quis dui viverra vestibulum. Suspendisse vulputate aliquam dui.</p>
  </article>
</section>

<main class="columns">
  <div class="col col-welcome">
    <h3><span class="lead">Welcome to Our</span><span class="strong">Website Mainpage</span></h3>
    <p>Mauris vel lacus vitae felis vestibulum volutpat. Etiam est nunc, venenatis in, tristique eu, imperdiet ac, nisl. Cum sociis natoque penatibus et magnis dis parturient montes, nascetur ridiculus mus. In iaculis facilisis massa. Etiam eu urna.</p>
    <p>Sed porta. Suspendisse quam leo, molestie sed, luctus quis, feugiat in, pede. Fusce tellus.</p>
  </div>
  <div class="col col-services">
    <h3>Services We Provide</h3>
    <p>Nunc tempus felis vitae urna. Vivamus port titor, g, purus nisi eleifend libero</p>
    <ul class="ticks">
      <li><svg width="16" height="13" viewBox="0 0 16 13"><path d="M1 7l4 4 10-10" fill="none" stroke="#2a1a18" stroke-width="2.6"/></svg>Phasellus felis dolor scelerisque</li>
      <li><svg width="16" height="13" viewBox="0 0 16 13"><path d="M1 7l4 4 10-10" fill="none" stroke="#2a1a18" stroke-width="2.6"/></svg>Tempus eget lobortis id libero.</li>
      <li><svg width="16" height="13" viewBox="0 0 16 13"><path d="M1 7l4 4 10-10" fill="none" stroke="#2a1a18" stroke-width="2.6"/></svg>Donec scelerisque leo ac risus.</li>
      <li><svg width="16" height="13" viewBox="0 0 16 13"><path d="M1 7l4 4 10-10" fill="none" stroke="#2a1a18" stroke-width="2.6"/></svg>Praesent sit amet est.</li>
    </ul>
  </div>
  <div class="col col-gallery">
    <h3>Our Gallery</h3>
    <div class="gallery">
      <div role="img" aria-label="Curved modern architecture" style="background:linear-gradient(150deg,#2b3a5a,#9aa4b8,#1f2530)"></div>
      <div role="img" aria-label="Warm lit living room" style="background:linear-gradient(150deg,#8a6a40,#d8c4a0,#9a8060)"></div>
      <div role="img" aria-label="Lounge with textured wall art" style="background:linear-gradient(150deg,#7c7c7c,#b7ab96,#e6e3de)"></div>
      <div role="img" aria-label="Timber deck at dusk" style="background:linear-gradient(150deg,#1e2f4a,#7a4a22,#3a2a1e)"></div>
      <div role="img" aria-label="Bright living area with cream sofa" style="background:linear-gradient(150deg,#3a3a32,#d8d0bc,#f2ede2)"></div>
      <div role="img" aria-label="Architectural plans on a desk" style="background:linear-gradient(150deg,#c8ccd4,#e8eaee,#b0a8a0)"></div>
    </div>
  </div>
</main>

<footer class="site-footer">
  <small>© 2013 Company Name.&nbsp; All right reserved.&nbsp; Term of Use</small>
  <nav class="footer-nav">
    <a href="#">MAIN</a><a href="#">ABOUT US</a><a href="#">SERVICES</a><a href="#">PROJECTS</a><a href="#">CONTACT</a>
  </nav>
</footer>

</body>
</html>
```